Kneadwell Bodycare Studio

We are a Massage Therapy business based in Invercargill, New Zealand. We specialise in Sports and deep tissue massage but also provide relaxation and aromatherapy massage. We would like to see designs that use the the logo.
The final design should promote health and fitness.
Updates

Hi I am getting feedback that my business card picture is poor quality. I got this picture from brightpress under massage. So if you google this image a better quality picture should come up,. If not hope to upload a better image by tomorow, thanks.

Target Market(s)

Sports, people with pain and injuries

Industry/Entity Type

Massage

Requirements
Must have
• Logo, muscle body that is used on the business card, also a poster that matches my business card
Nice to have
• Picture of muscle man, shown on my business card
Should not have
• Not a picture of a real person

```html
<!DOCTYPE html>
<html lang="en">
<head>
<meta charset="utf-8">
<title>Kneadwell Bodycare Studio — Poster</title>
<link rel="stylesheet" href="https://fonts.googleapis.com/css2?family=Archivo+Black&family=Arimo:wght@700&family=Roboto:wght@400&family=Roboto+Condensed:wght@400;700&display=swap">
<style>
  :root {
    --page-bg: #eceff2;
    --sheet-white: #ffffff;
    --sheet-sky: #bfe3f3;
    --sheet-sky-deep: #9fd2ec;
    --title-slate: #56657a;
    --ink: #1e1e1e;
    --bullet-brown: #b5712f;
    --price-head: #7b8799;
    --price-border: #8a95a6;
    --phone-ink: #4a4a4c;
    --phone-icon: #9a3a22;
    --address-red: #e0201f;
    --band-red: #d81f26;
    --band-red-deep: #a8141a;
    --ribbon-green: #2f5d2a;
    --ribbon-orange: #e2701f;
    --mark-pink: #e779b4;
    --figure-bone: #e6ded4;
    --figure-red: #c85a44;
    --figure-violet: #7c6a9c;
  }
  * { box-sizing: border-box; margin: 0; padding: 0; }
  html, body { width: 1000px; height: 1200px; overflow: hidden; }
  body { background: var(--page-bg); position: relative; font-family: "Roboto", Arial, sans-serif; }

  .poster {
    position: absolute; left: 75px; top: 0; width: 850px; height: 1200px; overflow: hidden;
    background:
      radial-gradient(ellipse 60% 55% at 95% 40%, var(--sheet-sky-deep) 0%, transparent 70%),
      linear-gradient(100deg, var(--sheet-white) 30%, var(--sheet-sky) 100%);
  }

  .corner-ribbon { position: absolute; left: 0; top: 0; width: 420px; height: 320px; }
  .corner-ribbon text { fill: #fff; font-family: "Roboto", Arial, sans-serif; letter-spacing: 2px; }

  .brand-mark {
    position: absolute; left: 465px; top: 35px; width: 120px; height: 120px; border-radius: 50%;
    background: var(--mark-pink); opacity: 0.85;
  }

  .brand-name {
    position: absolute; left: 200px; top: 190px; width: 610px; text-align: center;
    font-family: "Roboto Condensed", "Arial Narrow", sans-serif;
    font-weight: 400; font-size: 54px; color: var(--title-slate); letter-spacing: 0.5px; white-space: nowrap;
  }

  .anatomy-figure {
    position: absolute; left: 0; top: 245px; width: 420px; height: 690px;
    background: linear-gradient(180deg, var(--figure-bone) 0%, var(--figure-red) 30%, var(--figure-violet) 60%, var(--figure-red) 80%, rgba(255,255,255,0) 100%);
    opacity: 0.8;
  }

  .service-list { position: absolute; left: 420px; top: 315px; list-style: none; }
  .service-list li {
    font-size: 42px; font-weight: 400; color: var(--ink); line-height: 58px;
    display: flex; align-items: center;
  }
  .service-list li::before {
    content: ""; width: 20px; height: 20px; border-radius: 50%; background: var(--bullet-brown);
    margin-right: 18px; flex: none;
  }

  .price-table {
    position: absolute; left: 418px; top: 643px; width: 382px; height: 232px;
    border: 2px solid var(--price-border); border-radius: 3px; background: rgba(255,255,255,0.55);
  }
  .price-table__head {
    background: var(--price-head); color: #fff; text-align: center;
    font-size: 50px; font-weight: 400; height: 62px; line-height: 66px; letter-spacing: 1px;
  }
  .price-table__rows { list-style: none; padding-top: 6px; text-align: center; }
  .price-table__rows li { font-size: 38px; line-height: 52px; color: var(--ink); }

  .contact-phone { position: absolute; left: 80px; top: 908px; display: flex; align-items: center; }
  .contact-phone svg { width: 88px; height: 70px; margin-right: 14px; }
  .contact-phone__number {
    font-family: "Archivo Black", "Arial Black", sans-serif; font-size: 86px; color: var(--phone-ink);
    letter-spacing: 2px; line-height: 1;
  }

  .contact-address {
    position: absolute; left: 0; top: 993px; width: 850px; text-align: center;
    font-family: "Arimo", Arial, sans-serif; font-weight: 700; font-size: 41px; color: var(--address-red);
    white-space: nowrap;
  }

  .credential-band { position: absolute; left: 0; top: 1040px; width: 850px; height: 160px; }
  .credential-band svg { position: absolute; inset: 0; width: 100%; height: 100%; }
  .credential-band__text {
    position: relative; padding-top: 42px; text-align: center; color: #fff;
    font-family: "Roboto Condensed", "Arial Narrow", sans-serif;
    font-weight: 700; font-size: 42px; line-height: 50px; letter-spacing: 1.5px; white-space: nowrap;
  }
</style>
</head>
<body>
  <main class="poster">
    <div class="corner-ribbon">
      <svg width="420" height="320" viewBox="0 0 420 320" role="img" aria-label="ARE YOU IN PAIN?">
        <defs>
          <linearGradient id="ribbonFill" x1="0" y1="0" x2="0.4" y2="1">
            <stop offset="0" stop-color="var(--ribbon-green)"/>
            <stop offset="1" stop-color="var(--ribbon-orange)"/>
          </linearGradient>
        </defs>
        <polygon points="0,0 400,0 0,310" fill="url(#ribbonFill)"/>
        <text x="122" y="128" font-size="36" text-anchor="middle" transform="rotate(-36 122 128)">ARE YOU IN</text>
        <text x="165" y="175" font-size="46" text-anchor="middle" transform="rotate(-36 165 175)">PAIN?</text>
      </svg>
    </div>

    <div class="brand-mark" aria-hidden="true"></div>
    <h1 class="brand-name">Kneadwell Bodycare Studio</h1>

    <div class="anatomy-figure" role="img" aria-label="Anatomical illustration of a muscular back and shoulders seen from behind"></div>

    <ul class="service-list">
      <li>Deep Tissue</li>
      <li>Sports Massage</li>
      <li>Relaxation</li>
      <li>Aromatherapy</li>
      <li>Hot Stones</li>
    </ul>

    <section class="price-table">
      <h2 class="price-table__head">Prices</h2>
      <ul class="price-table__rows">
        <li>30minutes&nbsp; $40</li>
        <li>60minutes&nbsp; $60</li>
        <li>90 minutes $80</li>
      </ul>
    </section>

    <div class="contact-phone">
      <svg viewBox="0 0 92 70" aria-hidden="true">
        <path d="M8 22 C8 8 84 8 84 22 L84 30 L64 30 L64 22 L28 22 L28 30 L8 30 Z" fill="var(--phone-icon)"/>
        <path d="M22 32 L70 32 L86 64 L6 64 Z" fill="var(--phone-icon)"/>
        <circle cx="46" cy="48" r="11" fill="#fff"/>
        <circle cx="46" cy="48" r="5" fill="var(--phone-icon)"/>
      </svg>
      <span class="contact-phone__number">0274518826</span>
    </div>

    <p class="contact-address">48 HARLOW ST, INVERCARGILL 9810</p>

    <footer class="credential-band">
      <svg viewBox="0 0 850 160" preserveAspectRatio="none" aria-hidden="true">
        <defs>
          <linearGradient id="bandFill" x1="0" y1="0" x2="0" y2="1">
            <stop offset="0" stop-color="var(--band-red)"/>
            <stop offset="1" stop-color="var(--band-red-deep)"/>
          </linearGradient>
        </defs>
        <path d="M0 30 Q425 0 850 30 L850 160 L0 160 Z" fill="url(#bandFill)"/>
      </svg>
      <p class="credential-band__text">MIRA DALTON BACHELOR THERAPEIUTIC&amp;<br>SPORTS MASSAGE</p>
    </footer>
  </main>
</body>
</html>
```